Valtrop Fabrication Works - Project Portfolio *

We deal in structural steel and membrane works. Would like to have a brochure done with some of our more significant projects photos and description.
And of course our company background and services we provide.

Attached in the Zip file are some of the project photos that i would like to have inside the brochure.

Note that every project has a simple write up in it.

The power point slides has the company background info and some of the bigger projects that i want to include also.

Our main works is steel but we are venturing into membrane works too.

Target Market(s)

Business to Business

Industry/Entity Type

Steel

Font styles to use
Sans Serif

Colors

Designer to choose colors to be used in the design.

Requirements
Must have
• Photos showcasing the works we have done.
• Will also provide photos of our factory and facilities.
• And a brief background and services we provide.
Nice to have
• Cropped out photos so that the background will not be unrelated stuff.

```html
<!DOCTYPE html>
<html lang="en">
<head>
<meta charset="utf-8">
<title>Valtrop Fabrication Works – Project Portfolio</title>
<link href="https://fonts.googleapis.com/css2?family=Archivo:wght@400;700;800&family=Lato:wght@400;700&display=swap" rel="stylesheet">
<style>
:root{
  --stage:#2b2b2b;
  --paper:#ffffff;
  --paper-shade:#eeeeee;
  --red:#e8343b;
  --red-dark:#b9242a;
  --ink:#222222;
  --grey:#555555;
  --sky:#9fb4c6;
  --city:#6b6358;
  --steel:#8f9aa6;
}
*{margin:0;padding:0;box-sizing:border-box}
html,body{width:1130px;height:1200px;overflow:hidden;background:var(--stage)}
body{position:relative;font-family:"Lato",sans-serif;color:var(--ink)}
.spread{position:absolute;left:169px;width:792px;height:560px;display:flex;box-shadow:0 12px 30px rgba(0,0,0,.45)}
.spread--covers{top:20px}
.spread--projects{top:620px}
.page{position:relative;width:396px;height:560px;background:var(--paper);overflow:hidden}
.page--left{background:linear-gradient(90deg,var(--paper) 85%,var(--paper-shade))}
.page--right{background:linear-gradient(90deg,var(--paper-shade),var(--paper) 12%)}
.photo{position:absolute;background:linear-gradient(180deg,var(--sky),var(--steel) 55%,var(--city))}
.brand{display:flex;align-items:center;gap:6px;font-family:"Archivo",sans-serif;font-weight:700;font-size:11px;color:var(--ink);letter-spacing:.3px}
.brand__mark{width:18px;height:18px;border:2px solid var(--red)}

/* back cover */
.background{position:absolute;left:28px;top:34px;width:330px}
.background__title{font-family:"Archivo",sans-serif;font-weight:800;font-size:13px;color:var(--red);margin-bottom:8px}
.background p{font-size:8.5px;line-height:1.45;color:var(--grey);margin-bottom:5px}
.background__slogan{font-family:"Archivo",sans-serif;font-weight:700;font-size:10px;color:var(--ink);margin-top:6px}
.band{position:absolute;left:0;top:170px;width:396px;height:200px}
.contacts{position:absolute;left:30px;top:262px;list-style:none;color:#fff}
.contacts li{display:flex;align-items:center;gap:7px;font-size:8.5px;margin-bottom:4px}
.contacts li:first-child{font-size:11px;font-weight:700}
.contacts svg{width:9px;height:9px;fill:#fff}
.back-web{position:absolute;right:30px;bottom:64px;font-family:"Archivo",sans-serif;font-weight:700;font-size:10px}
.back-brand{position:absolute;left:30px;bottom:30px}

/* front cover */
.cover-photo{left:22px;top:14px;width:354px;height:478px;background:linear-gradient(180deg,#b7c5d2 0%,#a9b6c0 28%,var(--steel) 45%,var(--city) 75%,#4e4a44 100%)}
.cover-brand{position:absolute;left:40px;top:36px}
.cover-banner{position:absolute;left:62px;top:168px;width:314px;height:92px;background:rgba(232,52,59,.92);color:#fff;padding:14px 0 0 28px}
.cover-banner__title{font-family:"Archivo",sans-serif;font-weight:800;font-size:23px;letter-spacing:.2px}
.cover-banner__sub{font-family:"Archivo",sans-serif;font-weight:400;font-size:14px}
.cover-banner__web{font-size:8px;letter-spacing:3px;margin-top:4px}
.badges{position:absolute;left:220px;top:500px;display:flex;gap:8px}
.badge{width:40px;height:24px;border:1px solid #999;background:#f4f4f4}
.badge--wide{width:52px;background:#dfe6ee}

/* project pages */
.hero-photo{left:18px;top:24px;width:360px;height:250px}
.side-photo{top:282px;width:176px;height:150px}
.side-photo--a{left:18px;background:linear-gradient(180deg,#b6c6d6,#8796a8 55%,#c7b28f)}
.side-photo--b{left:202px;background:linear-gradient(180deg,#c9d3dc,#7d8ea3 60%,#b8bcc0)}
.caption{position:absolute;left:150px;top:452px;font-family:"Archivo",sans-serif;font-weight:800;font-size:13px;line-height:1.2;text-align:right;width:220px}
.caption__lead{color:var(--red)}
.caption__rest{font-weight:700;color:var(--ink);font-size:11px}
.folio{position:absolute;bottom:26px;display:flex;align-items:center;gap:6px}
.folio--left{left:18px;right:18px}
.folio--right{left:18px;right:18px}
.folio__num{width:14px;height:14px;background:var(--red);color:#fff;font-size:9px;font-weight:700;display:flex;align-items:center;justify-content:center}
.folio__rule{flex:1;height:2px;background:var(--red)}
.grid{position:absolute;left:18px;top:24px;width:360px;display:grid;grid-template-columns:1fr 1fr;gap:8px}
.tile{position:relative;height:148px}
.tile .photo{inset:0}
.tile__label{position:absolute;left:0;right:0;bottom:0;height:22px;background:var(--red);color:#fff;font-family:"Archivo",sans-serif;font-weight:700;font-size:8.5px;display:flex;align-items:center;justify-content:center;letter-spacing:.3px}
</style>
</head>
<body>

<section class="spread spread--covers">
  <article class="page page--left back-cover">
    <div class="background">
      <h2 class="background__title">COMPANY BACKGROUND</h2>
      <p>Started out since 1982.</p>
      <p>Valtrop Fabrication Works had since moved out of the Eastbank workshop to the current one at Northfield Industrial Park.</p>
      <p>In this area, we have 2 full fledged workshops with a total of 23,000 sqft.</p>
      <p>We are equipped with machineries and tools to handle steel and metal works of different scales. We are always learning from new technology, and what brought us so far today is a simple mindset.</p>
      <p class="background__slogan">FAST PRODUCTIVITY , QUALITY PRODUCTS &amp; SAFETY !</p>
    </div>
    <svg class="band" viewBox="0 0 396 200" preserveAspectRatio="none" aria-hidden="true">
      <path d="M0 60 Q200 40 396 0 L396 110 Q200 160 0 185 Z" fill="var(--red)"/>
      <path d="M0 185 Q200 160 396 110 L396 118 Q200 170 0 194 Z" fill="#333"/>
      <path d="M0 60 Q200 40 396 0 L396 40 Q200 70 0 85 Z" fill="var(--red-dark)" opacity=".35"/>
    </svg>
    <ul class="contacts">
      <li><svg viewBox="0 0 10 10"><path d="M2 0h2l1 3-1.5 1a6 6 0 0 0 2.5 2.5L7 5l3 1v2a2 2 0 0 1-2 2A8 8 0 0 1 0 2a2 2 0 0 1 2-2z"/></svg>6100 2400</li>
      <li><svg viewBox="0 0 10 10"><rect x="2" y="0" width="6" height="3"/><rect x="0" y="3" width="10" height="5"/><rect x="2" y="7" width="6" height="3"/></svg>6100 2401</li>
      <li><svg viewBox="0 0 10 10"><path d="M0 2h10v6H0z M0 2l5 3 5-3" stroke="#e8343b" stroke-width=".6"/></svg>info@valtropfab.com.sg</li>
      <li><svg viewBox="0 0 10 10"><path d="M5 0a3.5 3.5 0 0 1 3.5 3.5C8.5 6 5 10 5 10S1.5 6 1.5 3.5A3.5 3.5 0 0 1 5 0z"/></svg>18 Northfield Industrial Park Lane 3, Singapore 700118</li>
    </ul>
    <div class="back-web">www.valtropfab.com.sg</div>
    <div class="brand back-brand"><span class="brand__mark"></span>VALTROP FABRICATION WORKS</div>
  </article>

  <article class="page page--right front-cover">
    <div class="photo cover-photo" role="img" aria-label="City skyline with high-rise towers under a pale sky"></div>
    <div class="brand cover-brand"><span class="brand__mark"></span>VALTROP FABRICATION WORKS</div>
    <div class="cover-banner">
      <h1 class="cover-banner__title">FAST PRODUCTIVITY</h1>
      <p class="cover-banner__sub">QUALITY PRODUCTS &amp; SAFETY</p>
      <p class="cover-banner__web">www.valtropfab.com.sg</p>
    </div>
    <div class="badges"><span class="badge"></span><span class="badge badge--wide"></span></div>
  </article>
</section>

<section class="spread spread--projects">
  <article class="page page--left">
    <div class="photo hero-photo" role="img" aria-label="Wide span steel shed frame under construction with scaffolding and a lift"></div>
    <div class="photo side-photo side-photo--a" role="img" aria-label="Row of blue steel columns on a sandy site"></div>
    <div class="photo side-photo side-photo--b" role="img" aria-label="Interior of a long span shed roof structure"></div>
    <h2 class="caption"><span class="caption__lead">WIDE SPAN SHED &amp; ANCILLARY</span><br><span class="caption__rest">BASE WORKS AT EASTCOVE NAVAL BASE</span></h2>
    <div class="folio folio--left"><span class="folio__num">1</span><span class="folio__rule"></span></div>
  </article>

  <article class="page page--right">
    <div class="grid">
      <figure class="tile"><div class="photo" role="img" aria-label="Steel roof trusses against a blue sky"></div><figcaption class="tile__label">CARGO HUB @ HARBOUR AVE 10</figcaption></figure>
      <figure class="tile"><div class="photo" role="img" aria-label="Steel warehouse frame with gantry crane"></div><figcaption class="tile__label">WESTPOINT @ WESTFIELD ST 22</figcaption></figure>
      <figure class="tile"><div class="photo" role="img" aria-label="Dim interior of steel building frame"></div><figcaption class="tile__label">WESTPOINT @ WESTFIELD ST 22</figcaption></figure>
      <figure class="tile"><div class="photo" role="img" aria-label="Roof purlins over an open steel hall"></div><figcaption class="tile__label">WESTPOINT @ WESTFIELD ST 22</figcaption></figure>
      <figure class="tile"><div class="photo" role="img" aria-label="Fabricated steel trusses laid out in a yard"></div><figcaption class="tile__label">WESTPOINT @ WESTFIELD ST 22</figcaption></figure>
      <figure class="tile"><div class="photo" role="img" aria-label="Truss assembly beside a yellow crane"></div><figcaption class="tile__label">WESTPOINT @ WESTFIELD ST 22</figcaption></figure>
    </div>
    <div class="folio folio--right"><span class="folio__num">2</span><span class="folio__rule"></span></div>
  </article>
</section>

</body>
</html>
```